bmlk website

revamp of existing website...design only
brimlake.com.au
existing site a bit óld fashioned'...needs to be modernised and bright and cheery.
need: home page, second and third level pages.

end user/retail information website
this site does NOT need a shopping card as we do not sell direct to the public

• 3 levels
• home
• second level
• third level

```html
<!DOCTYPE html>
<html lang="en">
<head>
<meta charset="utf-8">
<title>Brimlake – Metal Storage Cabinets</title>
<link href="https://fonts.googleapis.com/css2?family=Source+Sans+3:wght@300;400;600;700&display=swap" rel="stylesheet">
<style>
:root{
  --red:#ed1c24;
  --dark-red:#c8141b;
  --black:#000;
  --ink:#333;
  --grey-text:#8a8a8a;
  --btn:#4a4a4a;
  --page:#f1f1f1;
  --card:#fff;
  --white:#fff;
  --steel-light:#e6e8ea;
  --steel:#b8bcc0;
  --steel-dark:#8d9196;
}
*{margin:0;padding:0;box-sizing:border-box}
html,body{width:911px;height:1200px;overflow:hidden}
body{font-family:"Source Sans 3",Arial,sans-serif;background:var(--page);color:var(--ink);position:relative}
a{color:inherit;text-decoration:none}

/* header */
.site-header{position:absolute;left:0;top:0;width:911px;height:92px;background:var(--red);color:var(--white)}
.brand{position:absolute;left:99px;top:22px;width:210px;text-align:right}
.brand-name{display:block;font-size:36px;font-weight:700;line-height:38px;text-align:left;letter-spacing:1.5px}
.brand-tag{display:block;font-size:12px;color:#1a1a1a;margin-top:2px}
.utility{position:absolute;top:18px;left:401px;font-size:10.5px;display:flex;align-items:center;gap:6px;height:14px}
.utility svg{display:block}
.search{position:absolute;left:638px;top:15px;width:188px;height:21px;background:var(--white);border-radius:2px;font-size:7px;color:#ccc;padding:6px 7px}
.search svg{position:absolute;right:5px;top:5px}
.main-nav{position:absolute;top:51px;left:429px;display:flex;font-size:13px}
.main-nav a{margin-right:28px}
.main-nav a:last-child{margin-right:0}

/* hero */
.hero{position:absolute;left:0;top:92px;width:911px;height:326px;background:var(--black);color:var(--white)}
.hero-photo{position:absolute;left:326px;top:0;width:540px;height:326px;
  background:
    linear-gradient(90deg,transparent 0,transparent 178px,rgba(20,20,20,.9) 178px,#1b1b1b 212px,#2c2c2c 280px,#1b1b1b 348px,rgba(20,20,20,.9) 366px,transparent 366px),
    radial-gradient(circle at 62% 48%,#3c3c3c,#1a1a1a 68%,#101010)}
.hero-copy{position:absolute;left:193px;top:53px}
.hero-kicker{color:var(--red);font-size:17.5px;font-weight:600;line-height:22px}
.hero-title{font-size:17.5px;font-weight:600;line-height:26px;margin-top:3px;width:240px}
.hero-list{list-style:none;font-size:11.2px;line-height:23px;margin-top:2px}
.hero-arrow{position:absolute;top:130px}

/* promos */
.promo{position:absolute;top:458px;width:348px;height:220px;background:var(--red);color:var(--white)}
.promo-cover{position:absolute;left:19px;top:17px;width:133px;height:187px;box-shadow:3px 4px 8px rgba(0,0,0,.4)}
.cover-catalogue{background:linear-gradient(180deg,#2a2a2a 0,#3a3a3a 30%,#c9cdd1 42%,#9ea3a8 55%,#d01820 60%,#d01820 66%,#1e1e1e 70%,#141414 100%)}
.cover-flyer{left:22px;background:linear-gradient(180deg,#d01820 0,#d01820 10%,#f4f4f4 12%,#d8b9b9 40%,#e9e9e9 58%,#cc1f26 62%,#cc1f26 65%,#c9ccd0 68%,#eef0f2 100%)}
.promo-body{position:absolute;left:181px;top:35px;width:154px}
.promo-title{font-size:21px;font-weight:700;line-height:22px}
.promo-title span{display:block;font-weight:300}
.promo-sub{font-size:9px;margin-top:3px}
.promo-text{font-size:9.4px;line-height:15.2px;margin-top:13px}
.btn{display:inline-block;background:var(--btn);color:var(--white);font-size:9.5px;padding:3px 7px}
.promo .btn{margin-top:10px}

/* products */
.section-title{position:absolute;left:100px;top:707px;font-size:14px;font-weight:700;color:var(--red)}
.pager{position:absolute;top:707px;width:24px;height:18px;display:flex;align-items:center;justify-content:center}
.product{position:absolute;top:747px;width:167px;height:243px;background:var(--card);text-align:center}
.product-photo{position:absolute;background:linear-gradient(90deg,var(--steel-dark) 0,var(--steel-light) 8%,var(--steel) 12%,#f2f2f2 14%,#d9c7b8 45%,#eee 55%,#c7cfd8 80%,var(--steel) 88%,var(--steel-light) 92%,var(--steel-dark) 100%)}
.product-name{position:absolute;left:0;right:0;top:143px;color:var(--red);font-size:11.5px;font-weight:600}
.product-spec{position:absolute;left:0;right:0;top:161px;color:var(--grey-text);font-size:11px;line-height:18px;font-weight:300}
.product .btn{position:absolute;left:38px;top:209px;width:91px;height:24px;padding:6px 0 0 7px;text-align:left}
.product .btn svg{position:absolute;right:8px;top:5px}

/* features */
.features{position:absolute;left:0;top:1043px;width:911px;height:79px;background:#f7f7f7;border-top:1px solid #e4e4e4}
.feature{position:absolute;top:0;height:79px;display:flex;align-items:center;font-size:10.5px;line-height:15px;color:#222}
.feature small{font-size:9px}
.feature-art{flex:none}
.divider{position:absolute;top:0;width:1px;height:79px;background:#e0e0e0}

/* footer */
.site-footer{position:absolute;left:0;top:1122px;width:911px;height:78px;background:var(--red);color:var(--white)}
.footer-nav{position:absolute;left:99px;top:25px;font-size:11px;display:flex}
.footer-nav a{padding:0 8px;border-left:1px solid var(--white)}
.footer-nav a:first-child{padding-left:0;border-left:0}
.copyright{position:absolute;left:99px;top:50px;font-size:11px}
.made-badge{position:absolute;left:654px;top:11px;width:56px;height:56px;border-radius:50%;background:#111}
.social{position:absolute;top:28px;width:28px;height:28px;border-radius:50%;background:var(--white)}
</style>
</head>
<body>

<header class="site-header">
  <a class="brand" href="#"><span class="brand-name">BRIMLAKE</span><span class="brand-tag">Metal Storage cabinets</span></a>
  <div class="utility">
    <span>1300-555 014</span><span>|</span>
    <span>Where to buy</span>
    <svg width="16" height="13" viewBox="0 0 16 13"><path d="M1 3h14l-2 9H3z" fill="none" stroke="#fff" stroke-width="1.4"/><path d="M6 5v5M10 5v5" stroke="#fff"/></svg>
    <span>|</span>
    <span>E-Mail Us</span>
    <svg width="18" height="12" viewBox="0 0 18 12"><rect x="1" y="1" width="16" height="10" fill="none" stroke="#fff" stroke-width="1.3"/><path d="M1 1l8 6 8-6" fill="none" stroke="#fff" stroke-width="1.3"/></svg>
  </div>
  <div class="search">Type search
    <svg width="10" height="10" viewBox="0 0 10 10"><circle cx="4" cy="4" r="3" fill="none" stroke="#999"/><path d="M6.3 6.3L9 9" stroke="#999"/></svg>
  </div>
  <nav class="main-nav"><a href="#">Home</a><a href="#">About Us</a><a href="#">Products</a><a href="#">Where to buy</a><a href="#">Who We Are ?</a></nav>
</header>

<section class="hero">
  <div class="hero-photo" role="img" aria-label="Open black metal storage cabinet holding tools, paint tins and a fuel can against a dark hexagon backdrop"></div>
  <div class="hero-copy">
    <h1 class="hero-kicker">Brimlake Cabinets</h1>
    <p class="hero-title">The easy and affordable storage solution for:</p>
    <ul class="hero-list"><li>• Workshops</li><li>• Garages</li><li>• Offices</li><li>• Archives</li><li>• Sports Rooms</li></ul>
  </div>
  <svg class="hero-arrow" style="left:72px" width="20" height="30" viewBox="0 0 20 30"><path d="M16 3L5 15l11 12" fill="none" stroke="#bbb" stroke-width="4"/></svg>
  <svg class="hero-arrow" style="left:818px" width="20" height="30" viewBox="0 0 20 30"><path d="M4 3l11 12L4 27" fill="none" stroke="#eee" stroke-width="4"/></svg>
</section>

<article class="promo" style="left:99px">
  <div class="promo-cover cover-catalogue" role="img" aria-label="Dark catalogue cover showing galvanised cabinets"></div>
  <div class="promo-body">
    <h2 class="promo-title">Download<span>Store</span></h2>
    <p class="promo-text">Lorem Ipsum is simply dummy text of the printing and typesetting industry. Lorem Ipsum has been the industry's standard dummy text ever since the 1500s, when an unknown printer</p>
    <a class="btn" href="#">Click Here</a>
  </div>
</article>

<article class="promo" style="left:465px">
  <div class="promo-cover cover-flyer" role="img" aria-label="Retail flyer showing cabinet styles and prices"></div>
  <div class="promo-body" style="top:33px">
    <h2 class="promo-title" style="font-size:22px">Brimlake</h2>
    <p class="promo-sub">Download Our Latest Retail Flyer</p>
    <p class="promo-text" style="margin-top:16px">Lorem Ipsum is simply dummy text of the printing and typesetting industry. Lorem Ipsum has been the industry's standard dummy text ever since the 1500s, when an unknown printer</p>
    <a class="btn" href="#">Click Here</a>
  </div>
</article>

<h2 class="section-title">OUR PRODUCTS</h2>
<a class="pager" href="#" style="left:759px;background:var(--red)"><svg width="8" height="10" viewBox="0 0 8 10"><path d="M6 1L2 5l4 4" fill="none" stroke="#fff" stroke-width="2"/></svg></a>
<a class="pager" href="#" style="left:788px;background:#6b6b6b"><svg width="8" height="10" viewBox="0 0 8 10"><path d="M2 1l4 4-4 4" fill="none" stroke="#fff" stroke-width="2"/></svg></a>

<div class="product" style="left:99px">
  <div class="product-photo" style="left:37px;top:15px;width:104px;height:108px" role="img" aria-label="Style 1 galvanised cabinet with half shelves and broom space"></div>
  <h3 class="product-name">STYLE 1 CABINET</h3>
  <p class="product-spec">Half Shelves, Half Broom Space<br>2 Lockable Doors</p>
  <a class="btn" href="#">Where to buy<svg width="16" height="13" viewBox="0 0 16 13"><path d="M1 3h14l-2 9H3z" fill="none" stroke="#fff" stroke-width="1.4"/><path d="M6 5v5M10 5v5" stroke="#fff"/></svg></a>
</div>
<div class="product" style="left:281px">
  <div class="product-photo" style="left:35px;top:15px;width:97px;height:108px" role="img" aria-label="Style 2 galvanised cabinet with full shelving"></div>
  <h3 class="product-name">STYLE 2 CABINET</h3>
  <p class="product-spec">Half Shelves, Half Broom Space<br>2 Lockable Doors</p>
  <a class="btn" href="#">Where to buy<svg width="16" height="13" viewBox="0 0 16 13"><path d="M1 3h14l-2 9H3z" fill="none" stroke="#fff" stroke-width="1.4"/><path d="M6 5v5M10 5v5" stroke="#fff"/></svg></a>
</div>
<div class="product" style="left:463px">
  <div class="product-photo" style="left:45px;top:13px;width:78px;height:118px;background:linear-gradient(180deg,#e9ecef,#c9d3d6 30%,#eef0f1 55%,#b7c4c2 75%,#f3f3f3)" role="img" aria-label="Style 3 open shelving unit with boxes and boots"></div>
  <h3 class="product-name">STYLE 3 CABINET</h3>
  <p class="product-spec">Half Shelves, Half Broom Space<br>2 Lockable Doors</p>
  <a class="btn" href="#">Where to buy<svg width="16" height="13" viewBox="0 0 16 13"><path d="M1 3h14l-2 9H3z" fill="none" stroke="#fff" stroke-width="1.4"/><path d="M6 5v5M10 5v5" stroke="#fff"/></svg></a>
</div>
<div class="product" style="left:645px">
  <div class="product-photo" style="left:16px;top:29px;width:136px;height:96px" role="img" aria-label="Counter height galvanised cabinet with doors open"></div>
  <h3 class="product-name">COUNTER HEIGHTS</h3>
  <p class="product-spec">Half Shelves, Half Broom Space<br>2 Lockable Doors</p>
  <a class="btn" href="#">Where to buy<svg width="16" height="13" viewBox="0 0 16 13"><path d="M1 3h14l-2 9H3z" fill="none" stroke="#fff" stroke-width="1.4"/><path d="M6 5v5M10 5v5" stroke="#fff"/></svg></a>
</div>

<section class="features">
  <div class="feature" style="left:123px">
    <div class="feature-art" role="img" aria-label="Map of Australia in flag colours" style="width:68px;height:54px;margin-right:24px;background:linear-gradient(135deg,#1f3a8a 40%,#c8141b 55%,#1f3a8a 70%);border-radius:12px"></div>
    <p>Galvanised Units<br>are Australian Made</p>
  </div>
  <div class="divider" style="left:326px"></div>
  <div class="feature" style="left:341px">
    <div class="feature-art" role="img" aria-label="Open delivery carton" style="width:58px;height:56px;margin-right:14px;background:linear-gradient(180deg,#f7b733 0,#f2a81f 35%,#e6e6e6 40%,#cfcfcf 100%)"></div>
    <p>Free Delivery - Brisbane Metro<br><small>(Delivery to business addresses only)</small></p>
  </div>
  <div class="divider" style="left:570px"></div>
  <div class="feature" style="left:585px">
    <div class="feature-art" role="img" aria-label="Boxes stacked on a shipping pallet" style="width:58px;height:58px;margin-right:11px;background:linear-gradient(180deg,#eef2f6 0,#cdd6e0 70%,#9a8a6c 85%,#6f6352 100%)"></div>
    <p>Orders from other areas welcome!<br><small>&nbsp;(Ask for a freight quote)</small></p>
  </div>
</section>

<footer class="site-footer">
  <nav class="footer-nav"><a href="#">Home</a><a href="#">About Us</a><a href="#">Products</a><a href="#">Where to buy</a><a href="#">Who We Are ?</a></nav>
  <p class="copyright">© 2013 Company Name ,All Rights Reserved</p>
  <div class="made-badge" role="img" aria-label="Locally made badge"></div>
  <a class="social" href="#" style="left:751px" aria-label="Social profile"></a>
  <a class="social" href="#" style="left:784px" aria-label="Social profile"></a>
</footer>

</body>
</html>
```